Vantrel BrewFuel needs a professional, modern and athlete appealing label for a square bottle

We need a label design for a new sports beverage drink called Vantrel BrewFuel. Looking for label that covers the front and back of the bottle, with the back showing the attached nutritional label. dimensions are below. This brewFuel will appeal to athletes and fitness enthusiast alike. product is all natural and made with pure cane sugar. no addictives, colorings or preservatives. there are three favors, so three separate colors/packaging will be needed but the same base design. Original which is black tea, lemon and pineapple are the 3 flavors. I would need the attached nutritional label incorporated into the label. Plastic Bottle Square : 2.4" Height : 7.3" Label panel: 4.6" Label panel area: 1.5" x 5" for one side

Target Market(s)

athletes and fitness enthusiast. both male and female between the ages of 13-35

Industry/Entity Type

It Professional

Requirements
Must have
• the name of the beverage Vantrel BrewFuel
• Made with real tea
• all natural
• Tea + Electrolytes

```html
<!DOCTYPE html>
<html lang="en">
<head>
<meta charset="utf-8">
<title>Vantrel BrewFuel – Label Range</title>
<link rel="stylesheet" href="https://fonts.googleapis.com/css2?family=Montserrat:wght@600;700;800;900&display=swap">
<style>
  :root {
    --brand-purple: #4f2d8a;
    --lemon-top: #e9d900;
    --lemon-low: #f6f0a8;
    --pineapple-top: #f0a11c;
    --pineapple-low: #fbe3c2;
    --original-top: #c41f24;
    --original-low: #f7e1dd;
    --badge-fill: #ffd61f;
    --badge-text: #e3261b;
    --label-white: #ffffff;
    --backdrop-top: #ffffff;
    --backdrop-bottom: #a9aaac;
  }
  html, body {
    margin: 0;
    padding: 0;
    width: 1200px;
    height: 1200px;
    overflow: hidden;
  }
  .canvas {
    width: 1200px;
    height: 1200px;
    background: linear-gradient(180deg, var(--backdrop-top) 0%, #e6e6e7 35%, var(--backdrop-bottom) 100%);
  }
  .canvas svg { display: block; }
  .brand-name {
    font-family: "Montserrat", sans-serif;
    font-weight: 600;
    font-size: 50px;
    fill: var(--brand-purple);
  }
  .claim-main {
    font-family: "Montserrat", sans-serif;
    font-weight: 900;
    font-size: 36px;
    fill: var(--brand-purple);
  }
  .claim-sub {
    font-family: "Montserrat", sans-serif;
    font-weight: 800;
    font-size: 13px;
    fill: var(--brand-purple);
  }
  .claim-note {
    font-family: "Montserrat", sans-serif;
    font-weight: 700;
    font-size: 9.5px;
    letter-spacing: 0.3px;
    fill: var(--brand-purple);
  }
  .flavor-name {
    font-family: "Montserrat", sans-serif;
    font-weight: 800;
    font-size: 12px;
    letter-spacing: 0.5px;
    fill: var(--badge-text);
  }
  .volume {
    font-family: "Montserrat", sans-serif;
    font-weight: 700;
    font-size: 12.5px;
    fill: var(--brand-purple);
  }
  .flavor-badge { fill: var(--badge-fill); stroke: var(--badge-text); stroke-width: 2; }
  .divider-band { stroke: var(--brand-purple); stroke-width: 8; }
</style>
</head>
<body>
<div class="canvas">
<svg width="1200" height="1200" viewBox="0 0 1200 1200" xmlns="http://www.w3.org/2000/svg">
  <defs>
    <path id="label-shape" d="M35,0 H248 Q283,0 283,35 L254.5,835 Q253,870 218,870 H65 Q30,870 29,835 L0,35 Q0,0 35,0 Z"/>
    <clipPath id="label-clip"><use href="#label-shape"/></clipPath>

    <linearGradient id="grad-lemon" x1="0" y1="0" x2="0" y2="1">
      <stop offset="0" stop-color="var(--lemon-top)"/>
      <stop offset="1" stop-color="var(--lemon-low)"/>
    </linearGradient>
    <linearGradient id="grad-pineapple" x1="0" y1="0" x2="0" y2="1">
      <stop offset="0" stop-color="var(--pineapple-top)"/>
      <stop offset="1" stop-color="var(--pineapple-low)"/>
    </linearGradient>
    <linearGradient id="grad-original" x1="0" y1="0" x2="0" y2="1">
      <stop offset="0" stop-color="var(--original-top)"/>
      <stop offset="1" stop-color="var(--original-low)"/>
    </linearGradient>

    <radialGradient id="art-lemon" cx="0.45" cy="0.5" r="0.55">
      <stop offset="0" stop-color="#fff3a0"/>
      <stop offset="0.7" stop-color="#f3d51c"/>
      <stop offset="1" stop-color="#8cc04a"/>
    </radialGradient>
    <radialGradient id="art-pineapple" cx="0.4" cy="0.55" r="0.6">
      <stop offset="0" stop-color="#fbe27a"/>
      <stop offset="0.65" stop-color="#e9c03a"/>
      <stop offset="1" stop-color="#5f8a3a"/>
    </radialGradient>
    <radialGradient id="art-original" cx="0.5" cy="0.55" r="0.55">
      <stop offset="0" stop-color="#b6e07a"/>
      <stop offset="1" stop-color="#4f9a2e"/>
    </radialGradient>

    <radialGradient id="floor-shadow" cx="0.5" cy="0.5" r="0.5">
      <stop offset="0" stop-color="#6f7072" stop-opacity="0.55"/>
      <stop offset="1" stop-color="#6f7072" stop-opacity="0"/>
    </radialGradient>
  </defs>

  <ellipse cx="277" cy="1105" rx="150" ry="30" fill="url(#floor-shadow)"/>
  <ellipse cx="602" cy="1105" rx="150" ry="30" fill="url(#floor-shadow)"/>
  <ellipse cx="927" cy="1105" rx="150" ry="30" fill="url(#floor-shadow)"/>

  <!-- Lemon label -->
  <g class="label label--lemon" transform="translate(136,160)">
    <g clip-path="url(#label-clip)">
      <use href="#label-shape" fill="var(--label-white)"/>
      <polygon points="0,0 283,0 283,446 -10,608" fill="url(#grad-lemon)"/>
      <line class="divider-band" x1="-10" y1="608" x2="293" y2="448"/>
    </g>
    <text class="brand-name" transform="translate(130,415) rotate(-90)">Vantrel</text>
    <text class="brand-name" transform="translate(190,415) rotate(-90)">BrewFuel</text>
    <text class="claim-main" transform="translate(138,516) rotate(-27.8)">TEA+</text>
    <text class="claim-sub" transform="translate(160,540) rotate(-27.8)">ELECTROLYTES</text>
    <rect role="img" aria-label="Lemon half with tea leaves illustration" x="84" y="610" width="150" height="140" rx="70" fill="url(#art-lemon)"/>
    <text class="claim-note" x="141.5" y="778" text-anchor="middle">MADE WITH REAL TEA · ALL NATURAL</text>
    <rect class="flavor-badge" x="105" y="794" width="73" height="20" rx="5"/>
    <text class="flavor-name" x="141.5" y="808.5" text-anchor="middle">LEMON</text>
    <text class="volume" x="141.5" y="834" text-anchor="middle">16 FL Oz (474 mL)</text>
  </g>

  <!-- Pineapple label -->
  <g class="label label--pineapple" transform="translate(461,160)">
    <g clip-path="url(#label-clip)">
      <use href="#label-shape" fill="var(--label-white)"/>
      <polygon points="0,0 283,0 283,446 -10,608" fill="url(#grad-pineapple)"/>
      <line class="divider-band" x1="-10" y1="608" x2="293" y2="448"/>
    </g>
    <text class="brand-name" transform="translate(130,415) rotate(-90)">Vantrel</text>
    <text class="brand-name" transform="translate(190,415) rotate(-90)">BrewFuel</text>
    <text class="claim-main" transform="translate(138,516) rotate(-27.8)">TEA+</text>
    <text class="claim-sub" transform="translate(160,540) rotate(-27.8)">ELECTROLYTES</text>
    <rect role="img" aria-label="Sliced pineapple illustration" x="56" y="620" width="180" height="130" rx="55" fill="url(#art-pineapple)"/>
    <text class="claim-note" x="141.5" y="778" text-anchor="middle">MADE WITH REAL TEA · ALL NATURAL</text>
    <rect class="flavor-badge" x="93" y="794" width="97" height="20" rx="5"/>
    <text class="flavor-name" x="141.5" y="808.5" text-anchor="middle">PINEAPPLE</text>
    <text class="volume" x="141.5" y="834" text-anchor="middle">16 FL Oz (474 mL)</text>
  </g>

  <!-- Original label -->
  <g class="label label--original" transform="translate(786,160)">
    <g clip-path="url(#label-clip)">
      <use href="#label-shape" fill="var(--label-white)"/>
      <polygon points="0,0 283,0 283,446 -10,608" fill="url(#grad-original)"/>
      <line class="divider-band" x1="-10" y1="608" x2="293" y2="448"/>
    </g>
    <text class="brand-name" transform="translate(130,415) rotate(-90)">Vantrel</text>
    <text class="brand-name" transform="translate(190,415) rotate(-90)">BrewFuel</text>
    <text class="claim-main" transform="translate(138,516) rotate(-27.8)">TEA+</text>
    <text class="claim-sub" transform="translate(160,540) rotate(-27.8)">ELECTROLYTES</text>
    <rect role="img" aria-label="Fresh green tea leaves illustration" x="52" y="615" width="190" height="135" rx="65" fill="url(#art-original)"/>
    <text class="claim-note" x="141.5" y="778" text-anchor="middle">MADE WITH REAL TEA · ALL NATURAL</text>
    <rect class="flavor-badge" x="102" y="794" width="79" height="20" rx="5"/>
    <text class="flavor-name" x="141.5" y="808.5" text-anchor="middle">ORIGINAL</text>
    <text class="volume" x="141.5" y="834" text-anchor="middle">16 FL Oz (474 mL)</text>
  </g>
</svg>
</div>
</body>
</html>
```